Modern and professional facebook ad for disability service

Design a facebook ad for a disability service. Want something bright and fun and eyecatching. Would ideally like a carousel ad as this will give us more options to provide information.
CONTENT:
- Looking for a Plan Manager who will support your TRBK journey so that you can focus on living your best possible life and achieve your TRBK Goals?
- Then join the Wattle Plan Management family today - quick and easy sign up.
- Friendly, Reliable, Responsive Service
- Dedicate Plan Managers so you always speak to the same person
- Fast Payment of Provider Invoices
- Supporting you to live Your Life, Your Way
- Call us today on 1300 482 613
- www.wattleplanmanagement.com.au

Sick

Target Market(s)

Disability Sector

Font styles to use
Other font styles liked:
• Raleway

Requirements
Must have
• Bright colours and eye catching design

```html
<!DOCTYPE html>
<html lang="en">
<head>
<meta charset="utf-8">
<title>Wattle Plan Management – Live Your Life, Your Way</title>
<link rel="stylesheet" href="https://fonts.googleapis.com/css2?family=Open+Sans:wght@700&family=Raleway:wght@600;700&display=swap">
<style>
  :root {
    --purple-deep: #8c0c86;
    --purple-mid: #b3009c;
    --purple-light: #b54bd2;
    --photo-green: #2fae4e;
    --photo-green-dark: #23863c;
    --ink-purple: #5f2a78;
    --brand-maroon: #a8325f;
    --white: #ffffff;
  }
  html, body {
    margin: 0;
    padding: 0;
    width: 1200px;
    height: 1200px;
    overflow: hidden;
    background: var(--white);
  }
  .ad {
    position: relative;
    width: 1200px;
    height: 1200px;
    overflow: hidden;
    background: var(--white);
  }
  .ad__shapes {
    position: absolute;
    inset: 0;
    width: 1200px;
    height: 1200px;
  }
  .headline {
    position: absolute;
    left: 28px;
    top: 150px;
    margin: 0;
    font-family: "Open Sans", sans-serif;
    font-weight: 700;
    font-size: 64px;
    line-height: 84px;
    color: var(--white);
    letter-spacing: 0.3px;
  }
  .contact {
    position: absolute;
    left: 0;
    width: 892px;
    margin: 0;
    text-align: center;
    font-family: "Raleway", sans-serif;
    font-weight: 600;
    color: var(--ink-purple);
    white-space: nowrap;
  }
  .contact--phone {
    top: 752px;
    font-size: 46px;
  }
  .contact--web {
    top: 826px;
    font-size: 46px;
  }
  .brand {
    position: absolute;
    left: 0;
    width: 892px;
    top: 1030px;
    display: flex;
    justify-content: center;
    align-items: center;
    gap: 16px;
    font-family: "Raleway", sans-serif;
    font-weight: 700;
    font-size: 34px;
    color: var(--brand-maroon);
    white-space: nowrap;
  }
  .brand__square {
    width: 34px;
    height: 34px;
    background: var(--brand-maroon);
  }
</style>
</head>
<body>
  <main class="ad">
    <svg class="ad__shapes" viewBox="0 0 1932 1932" xmlns="http://www.w3.org/2000/svg">
      <defs>
        <linearGradient id="purpleBand" x1="0" y1="0" x2="1" y2="0">
          <stop offset="0" stop-color="var(--purple-deep)"/>
          <stop offset="0.35" stop-color="var(--purple-mid)"/>
          <stop offset="0.7" stop-color="#b414a8"/>
          <stop offset="1" stop-color="var(--purple-light)"/>
        </linearGradient>
        <linearGradient id="photoTone" x1="0" y1="0" x2="0.4" y2="1">
          <stop offset="0" stop-color="var(--photo-green)"/>
          <stop offset="0.6" stop-color="#2a9c47"/>
          <stop offset="1" stop-color="var(--photo-green-dark)"/>
        </linearGradient>
      </defs>
      <path class="purple-band" fill="url(#purpleBand)"
            d="M0 0 H1932 V420 L1000 960 C820 1030 620 1050 430 1030 C260 1010 110 930 0 860 Z"/>
      <path class="photo-area" role="img"
            aria-label="Photo: two smiling young people taking a selfie outdoors, one seated in a wheelchair, tinted green"
            fill="url(#photoTone)"
            d="M805 690 C805 300 1150 80 1500 80 C1700 80 1840 110 1932 150 L1932 1932 L1390 1932
               C1560 1760 1650 1520 1570 1340 C1470 1180 1280 1175 1120 1135 C960 1095 870 980 835 860
               C815 800 805 740 805 690 Z"/>
    </svg>

    <h1 class="headline">Supporting you to<br>Live Your Life,<br>Your Way</h1>

    <p class="contact contact--phone">Call us today on 1300 482 613</p>
    <p class="contact contact--web">www.wattleplanmanagement.com.au</p>

    <div class="brand">
      <span class="brand__square"></span>
      <span class="brand__name">Wattle Plan Management</span>
    </div>
  </main>
</body>
</html>
```